依頼詳細
ページに使用したいキャッチフレーズ:
個性的な道を究め、劇的に生きる人生を選択する
それがMoonhollow

参考にしたいURL:
https://www.kenmori-ux.brelo.jp/
https://www.sorimachikeigo.com/member-lounge

ムーンホロウクラブのHP:
https://www.ruvo.co.jp/moonhollow/

ページに使用したいテキスト:
『Moonhollow Clubとは

「あなたの好きなことは何ですか?」
好きなことを徹底追求し、“好き”を個性に。
そして、個性を武器にしながら“才能”へと伸ばしていくことで、
人生の構想力が磨かれ、あなたの人生は切り拓かれていきます。

誰かに敷かれたレールに乗りたいのか?
型にはまらない人生を創造したいのか?
一度きりの人生を、自分はどう生きたいか?

「自分らしい」人生を実現しよう!。』

採択後、デザインに利用した、デザインデータもお送りください。
(特に、画像ファイルは必ず送ってください)

何かご不明な点がございましたら、お気軽にお申し付けください。

※ 過去の制作実績をそのままご提案いただいたり、他社のポートフォリオをそのまま掲載することは恐れ入りますが、ご遠慮いただけますと幸いです。
サイトURL
http://moonhollowclub.jp
ページ数
1ページ
希望イメージ
シンプル 複雑
単色 カラフル
暗い 明るい
日常 高級
遊び心 厳粛
未来的 伝統的
女性的 男性的
希望する色
赤系、黄・オレンジ系、ジェンダーニュートラルなデザイン
納品ファイル
• イラストレーター形式 (.ai)
• PNG形式 (.png)
補足説明
デザインに利用した、デザインデータ(画像など)もお送り頂きますようお願い致します。

素晴らしいデザインをありがとうございました。

素晴らしいデザインをありがとうございました。

```html
<!DOCTYPE html>
<html lang="ja">
<head>
<meta charset="utf-8">
<title>Moonhollow Club</title>
<link href="https://fonts.googleapis.com/css2?family=Noto+Sans+JP:wght@400;500;700&family=Dancing+Script:wght@500&display=swap" rel="stylesheet">
<style>
:root{
  --coral:#ef5f5c;
  --orange:#f2845a;
  --yellow:#ecd25c;
  --blush:#fdf0ef;
  --mist:#f3f3f3;
  --ink:#333333;
  --muted:#777777;
  --white:#ffffff;
  --thumb:#e2e2e2;
}
*{margin:0;padding:0;box-sizing:border-box}
html,body{width:1200px;height:4236px;overflow:hidden}
body{position:relative;background:var(--white);font-family:"Noto Sans JP",sans-serif;color:var(--ink)}
.abs{position:absolute}
.script{position:absolute;font-family:"Dancing Script",cursive;color:var(--coral);opacity:.35;font-size:96px;line-height:1;white-space:nowrap}
.sec-title{position:absolute;left:0;width:1200px;text-align:center;font-size:20px;font-weight:500;letter-spacing:.05em}
.sec-title::after{content:"";display:block;width:200px;height:3px;background:var(--coral);margin:14px auto 0}
.btn{position:absolute;background:var(--coral);color:var(--white);font-size:13px;text-align:center;line-height:48px;height:48px;width:184px;letter-spacing:.05em}
.tag{display:inline-block;border:1px solid var(--coral);color:var(--coral);font-size:10px;border-radius:10px;padding:0 10px;line-height:16px}
.photo{position:absolute}

/* header */
.site-header{position:absolute;top:0;left:0;width:1200px;height:100px;z-index:2}
.logo{position:absolute;left:48px;top:28px;font-size:30px;color:var(--coral);font-weight:500}
.gnav{position:absolute;right:160px;top:42px;display:flex;gap:30px;font-size:13px;color:var(--ink)}
.head-btn{position:absolute;right:0;width:140px;height:52px;background:var(--coral);color:var(--white);font-size:13px;display:flex;align-items:center;justify-content:center}
.head-btn.login{top:0;background:var(--orange)}
.head-btn.join{top:56px}

/* hero */
.hero{position:absolute;top:0;left:0;width:1200px;height:640px;background:linear-gradient(180deg,#f1ede6 0%,#e4dbcf 35%,#b9aa95 65%,#6b5846 100%)}
.hero-copy{position:absolute;top:420px;width:1200px;text-align:center;color:var(--white);font-size:19px;letter-spacing:.12em;line-height:68px;text-shadow:0 1px 6px rgba(0,0,0,.35)}

/* about */
.about-title{position:absolute;left:200px;top:730px;width:320px;text-align:center;font-size:20px;font-weight:500}
.about-title::after{content:"";display:block;height:3px;background:var(--coral);margin-top:14px}
.about-text{position:absolute;left:600px;top:780px;font-size:14px;line-height:28px}
.about-text p{margin-bottom:26px}
.about-bg{position:absolute;left:680px;top:1000px;width:520px;height:320px;background:var(--mist)}

/* news */
.news{position:absolute;left:128px;top:1300px;width:944px;height:520px;background:var(--blush)}
.news-list{position:absolute;left:200px;top:1488px;width:800px;font-size:13px}
.news-list li{list-style:none;display:flex;align-items:center;gap:26px;height:48px}

/* video */
.video-band{position:absolute;left:928px;top:1640px;width:272px;height:480px;background:var(--orange)}
.cards{position:absolute;display:flex}
.card .thumb{background:var(--thumb);display:flex;align-items:center;justify-content:center}
.card .meta{font-size:12px;margin-top:14px;display:flex;gap:18px;align-items:center}
.card .ttl{font-size:13px;margin-top:6px}

/* survey */
.survey-box{position:absolute;left:248px;top:2512px;width:712px;height:288px;background:var(--mist)}
.yellow-band{position:absolute;left:0;top:2712px;width:1200px;height:160px;background:var(--yellow)}
.survey-card{position:absolute;left:400px;top:2600px;width:560px;height:200px;background:var(--white)}

/* contact */
.contact-box{position:absolute;left:140px;top:3600px;width:940px;height:200px;background:rgba(255,255,255,.94);box-shadow:0 2px 14px rgba(0,0,0,.12)}
.contact-title{position:absolute;left:180px;top:3628px;font-size:20px;font-weight:500}
.contact-title::after{content:"";display:block;width:200px;height:3px;background:var(--coral);margin-top:12px}
.contact-text{position:absolute;left:440px;top:3664px;width:600px;font-size:13px;line-height:22px}

/* footer */
.footer{position:absolute;left:0;top:3840px;width:1200px;height:280px;background:var(--blush)}
.foot-bar{position:absolute;left:0;top:4120px;width:1200px;height:116px;background:var(--coral);color:var(--white)}
</style>
</head>
<body>

<section class="hero">
  <div class="photo" role="img" aria-label="霧の中へ真っすぐ伸びる線路の写真" style="inset:0"></div>
  <p class="hero-copy">個性的な道を究め、劇的に生きる人生を選択する<br>それがMoonhollow</p>
</section>

<header class="site-header">
  <div class="logo">Moonhollow Club</div>
  <nav class="gnav"><span>HOME</span><span>お知らせ</span><span>チャットルーム</span><span>新着動画</span><span>ブログ</span><span>アンケート</span><span>お問合せ</span></nav>
  <div class="head-btn login">ログイン</div>
  <div class="head-btn join">会員登録</div>
</header>

<!-- about -->
<div class="about-bg"></div>
<h2 class="about-title">Moonhollow Clubとは</h2>
<div class="photo" role="img" aria-label="アスファルトに描かれた分かれ道の矢印と足元の写真" style="left:128px;top:832px;width:384px;height:328px;background:linear-gradient(135deg,#5a5a5a,#3b3b3b)"></div>
<div class="about-text">
  <p>「あなたの好きなことは何ですか?」<br>好きなことを徹底追求し、“好き”を個性に。<br>そして、個性を武器にしながら“才能”へと伸ばしていくことで、<br>人生の構想力が磨かれ、あなたの人生は切り拓かれていきます。</p>
  <p>誰かに敷かれたレールに乗りたいのか?<br>型にはまらない人生を創造したいのか?<br>一度きりの人生を、自分はどう生きたいか?</p>
  <p>「自分らしい」人生を実現しよう!</p>
</div>
<div class="script" style="left:780px;top:990px;transform:rotate(-12deg)">about us</div>

<!-- news -->
<section class="news"></section>
<div class="script" style="left:100px;top:1310px;transform:rotate(-12deg)">news</div>
<h2 class="sec-title" style="top:1340px">お知らせ</h2>
<ul class="news-list">
  <li><span>2023.03.01</span><span class="tag">category</span><span>ホームページを開設しました</span></li>
  <li><span>2023.01.06</span><span class="tag">category</span><span>新年のご挨拶</span></li>
  <li><span>2022.12.23</span><span class="tag">category</span><span>年末年始イベントのご案内</span></li>
</ul>
<div class="btn" style="left:508px;top:1724px">more</div>

<!-- video -->
<div class="video-band"></div>
<div class="script" style="left:940px;top:1900px;color:var(--white);opacity:.5;transform:rotate(-12deg)">video</div>
<h2 class="sec-title" style="top:1936px">新着動画</h2>
<div class="cards" style="left:48px;top:2064px;gap:16px">
  <div class="card" style="width:264px"><div class="thumb" style="height:144px"><svg width="40" height="40" viewBox="0 0 40 40"><circle cx="20" cy="20" r="18" fill="none" stroke="#fff" stroke-width="2"/><path d="M16 12l12 8-12 8z" fill="#fff"/></svg></div><div class="meta"><span>2023.01.01.</span><span class="tag">category</span></div><div class="ttl">タイトルタイトル</div></div>
  <div class="card" style="width:264px"><div class="thumb" style="height:144px"><svg width="40" height="40" viewBox="0 0 40 40"><circle cx="20" cy="20" r="18" fill="none" stroke="#fff" stroke-width="2"/><path d="M16 12l12 8-12 8z" fill="#fff"/></svg></div><div class="meta"><span>2023.01.01.</span><span class="tag">category</span></div><div class="ttl">タイトルタイトル</div></div>
  <div class="card" style="width:264px"><div class="thumb" style="height:144px"><svg width="40" height="40" viewBox="0 0 40 40"><circle cx="20" cy="20" r="18" fill="none" stroke="#fff" stroke-width="2"/><path d="M16 12l12 8-12 8z" fill="#fff"/></svg></div><div class="meta"><span>2023.01.01.</span><span class="tag">category</span></div><div class="ttl">タイトルタイトル</div></div>
  <div class="card" style="width:264px"><div class="thumb" style="height:144px"><svg width="40" height="40" viewBox="0 0 40 40"><circle cx="20" cy="20" r="18" fill="none" stroke="#fff" stroke-width="2"/><path d="M16 12l12 8-12 8z" fill="#fff"/></svg></div><div class="meta"><span>2023.01.01.</span><span class="tag">category</span></div><div class="ttl">タイトルタイトル</div></div>
</div>
<div class="btn" style="left:508px;top:2360px">video list</div>

<!-- survey -->
<div class="survey-box"></div>
<div class="yellow-band"></div>
<div class="script" style="left:130px;top:2540px;transform:rotate(-12deg)">survey</div>
<div class="survey-card"></div>
<h2 class="sec-title" style="left:0;top:2620px">アンケート</h2>
<p class="abs" style="left:400px;top:2700px;width:560px;text-align:center;font-size:13px;line-height:22px">Moonhollow Clubのアンケート調査を行っております。<br>ご協力宜しくお願い致します。</p>
<div class="btn" style="left:832px;top:2734px;width:128px;height:44px;line-height:44px">click</div>
<div class="photo" role="img" aria-label="チェックリストとペンのイラスト" style="left:1020px;top:2560px;width:140px;height:240px;background:linear-gradient(180deg,#fafafa,#e6e6e6);border-radius:6px"></div>

<!-- blog -->
<div class="script" style="left:960px;top:2980px;transform:rotate(-12deg)">blog</div>
<h2 class="sec-title" style="top:2956px">ブログ</h2>
<div class="cards" style="left:192px;top:3092px;gap:16px">
  <div class="card" style="width:256px"><div class="thumb" style="height:148px"></div><div class="meta"><span>2023.01.01.</span><span class="tag">category</span></div><div class="ttl">タイトルタイトル</div></div>
  <div class="card" style="width:256px"><div class="thumb" style="height:148px"></div><div class="meta"><span>2023.01.01.</span><span class="tag">category</span></div><div class="ttl">タイトルタイトル</div></div>
  <div class="card" style="width:256px"><div class="thumb" style="height:148px"></div><div class="meta"><span>2023.01.01.</span><span class="tag">category</span></div><div class="ttl">タイトルタイトル</div></div>
</div>
<div class="btn" style="left:508px;top:3396px">blog list</div>

<!-- contact -->
<div class="photo" role="img" aria-label="ノートパソコンで作業する人物の手元の写真" style="left:0;top:3540px;width:600px;height:300px;background:linear-gradient(135deg,#d8d4d0,#9a918b)"></div>
<div class="contact-box"></div>
<div class="script" style="left:470px;top:3690px;opacity:.2;transform:rotate(-12deg)">contact</div>
<h2 class="contact-title">お問合せ</h2>
<p class="contact-text">Moonhollow Clubに関するご質問、ご意見、チャットルーム等のご利用方法はこちらからお問合せください。</p>
<div class="btn" style="left:880px;top:3736px;width:160px;height:44px;line-height:44px">click</div>

<!-- footer -->
<footer class="footer">
  <div class="abs" style="left:0;top:80px;width:1200px;text-align:center;font-size:30px;color:var(--coral);font-weight:500">Moonhollow Club</div>
  <div class="abs" style="left:460px;top:164px;width:130px;height:40px;background:var(--coral);color:var(--white);font-size:13px;line-height:40px;text-align:center">ログイン</div>
  <div class="abs" style="left:610px;top:164px;width:130px;height:40px;background:var(--orange);color:var(--white);font-size:13px;line-height:40px;text-align:center">会員登録</div>
</footer>
<div class="foot-bar">
  <nav class="abs" style="left:0;top:36px;width:1200px;display:flex;justify-content:center;gap:30px;font-size:13px"><span>HOME</span><span>お知らせ</span><span>チャットルーム</span><span>新着動画</span><span>ブログ</span><span>アンケート</span><span>お問合せ</span><span>利用規約</span><span>個人情報保護規程</span></nav>
  <p class="abs" style="left:0;top:80px;width:1200px;text-align:center;font-size:10px">Copyright Moonhollow Club All Rights Reserved.</p>
</div>

</body>
</html>
```